Corporate brochure design 4 pages

Hi,

We are a real estate company based in Europe.

We have almost finalized a rebranding.

We are developing a brand book guidelines (still on working process) to help you undertstand the look and feel of our new CI. I would like to receive proposals of design for a corporate brochure template. I need to receive the Indesign files with full ownership rights to be able to adapt all our documentation with this template.
Regarding the images, you can take gabaris on www.velmorastills.example. I will be able to take them afterwards.

There will be 4 pages. you will receive the 4 pages on pdf for your consideration with our (almost) actual layout.

- 1st page: cover
- 2nd page: company presentation in french and english
- 3rd page: some market data + graph
- 4th page: 2 retail centers presentation.

In the template, i need to have:
- the paragraph styles in order
- 2 different masters with top/bottom/page number aso.

Please feel free to ask any other questions.

best regards,
Updates

I would like to precise tha t we are active on the commercial real estate sector:

- office transactions (rent /sales)
- property management of administrative and business buildings
- Valuation of properties
- Capital markets (investment advices for selling building)

Industry/Entity Type

Real Estate

Colors

Designer to choose colors to be used in the design.

```html
<!DOCTYPE html>
<html lang="en">
<head>
<meta charset="utf-8">
<title>Corporate brochure – spread</title>
<link href="https://fonts.googleapis.com/css2?family=Marcellus&family=Arimo&family=Roboto+Condensed&display=swap" rel="stylesheet">
<style>
  :root {
    --orange: #f26a21;
    --ink: #231f20;
    --paper: #ffffff;
    --axis: #b3b3b3;
  }
  * { box-sizing: border-box; margin: 0; padding: 0; }
  html, body { width: 1200px; height: 928px; overflow: hidden; background: var(--paper); }
  .spread { position: relative; width: 1200px; height: 928px; font-family: "Arimo", Arial, sans-serif; color: var(--ink); }
  .top-rule { position: absolute; top: 0; left: 0; width: 1200px; height: 13px; background: var(--orange); }
  .page-fold { position: absolute; left: 600px; top: 0; width: 1px; height: 928px; background: var(--ink); z-index: 3; }

  .page-title {
    position: absolute; top: 35px; height: 64px;
    font-family: "Marcellus", Georgia, serif; font-weight: 400; font-size: 45px;
    color: var(--paper); line-height: 64px; letter-spacing: 1px;
  }
  .page-title--left { left: 0; width: 586px; padding-left: 32px; background: var(--orange); border-radius: 0 32px 32px 0; }
  .page-title--right { left: 614px; width: 586px; padding-left: 22px; background: var(--ink); border-radius: 32px 0 0 32px; }

  .lang-tab {
    position: absolute; top: 144px; height: 31px; width: 185px;
    font-family: "Marcellus", Georgia, serif; font-size: 27px; color: var(--paper);
    text-align: center; line-height: 31px;
  }
  .lang-tab--fr { left: 120px; background: var(--ink); border-radius: 16px 0 0 16px; line-height: 36px; }
  .lang-tab--en { left: 306px; background: var(--orange); border-radius: 0 16px 16px 0; line-height: 29px; }

  .body-copy { font-size: 13.4px; line-height: 16.2px; }
  .body-copy p + p { margin-top: 16px; }
  .column { position: absolute; top: 188px; width: 262px; }
  .column--fr { left: 35px; }
  .column--en { left: 317px; }
  .column-rule { position: absolute; left: 305px; top: 191px; width: 1px; height: 640px; background: var(--ink); }

  .market-copy { position: absolute; left: 620px; top: 124px; width: 566px; }
  .market-copy p + p { margin-top: 9px; }
  .market-copy p.spaced { margin-top: 17px; }

  .trend-chart { position: absolute; left: 600px; top: 369px; width: 600px; height: 462px; }
  .trend-chart text { font-family: "Marcellus", Georgia, serif; }

  .footer { position: absolute; left: 0; top: 846px; width: 1200px; height: 82px; background: var(--ink); }
  .footer-bar {
    position: absolute; left: 17px; top: 1px; width: 1166px; height: 26px;
    background: var(--orange); border: 2px solid var(--paper); border-radius: 13px;
  }
  .footer-url, .footer-call { position: absolute; width: 600px; text-align: center; }
  .footer-url { top: 3px; font-size: 16px; line-height: 22px; color: var(--ink); }
  .footer-call { top: 34px; color: var(--orange); font-family: "Roboto Condensed", "Arial Narrow", sans-serif; }
  .footer-call .label { font-size: 27px; }
  .footer-call .number { font-size: 36px; }
  .footer .left { left: -17px; }
  .footer .right { left: 600px; }
  .footer-call.right { left: 617px; }
</style>
</head>
<body>
<div class="spread">
  <div class="top-rule"></div>

  <h1 class="page-title page-title--left">Company presentation</h1>
  <h1 class="page-title page-title--right">Recent trends in market</h1>

  <div class="lang-tab lang-tab--fr">French</div>
  <div class="lang-tab lang-tab--en">English</div>

  <div class="column column--fr body-copy">
    <p>Lorem ipsum dolor sit amet, consectetur adipisicing elit, sed do eiusmod tempor incididunt ut labore et dolore magna aliqua. Ut enim ad minim veniam, quis nostrud exercitation ullamco laboris nisi ut aliquip ex ea commodo consequa.Lorem ipsum dolor sit amet, consectetur adipisicing elit, sed do eiusmod tempor incididunt ut labore et dolore magna aliqua. Ut enim ad minim veniam, quis.</p>
    <p>Lorem ipsum dolor sit amet, consectetur adipisicing elit, sed do eiusmod tempor incididunt ut labore et dolore magna aliqua. Ut enim ad minim veniam, quis nostrud exercitation ullamco laboris nisi ut aliquip ex ea commodo consequa.Lorem ipsum dolor sit amet, consectetur adipisicing elit, sed do eiusmod tempor incididunt ut labore et dolore magna aliqua. Ut enim ad minim veniam, quis.</p>
    <p>Lorem ipsum dolor sit amet, consectetur adipisicing elit, sed do eiusmod tempor incididunt ut labore et dolore magna aliqua. Ut enim ad minim veniam, quis nostrud exercitation ullamco laboris nisi ut aliquip ex ea commodo consequa.Lorem ipsum dolor sit amet, consectetur adipisicing elit, sed do eiusmod tempor incididunt ut labore et dolore magna aliqua. Ut enim ad minim veniam, quis.</p>
    <p>Lorem ipsum dolor sit amet, consectetur adipisicing elit, sed do eiusmod tempor incididunt ut labore et dolore magna aliqua. Ut enim ad minim veniam, quis nostrud exercitation ullamco laboris nisi ut aliquip ex ea commodo consequa.Lorem ipsum dolor sit amet, consectetur adipisicing.</p>
  </div>
  <div class="column-rule"></div>
  <div class="column column--en body-copy">
    <p>Lorem ipsum dolor sit amet, consectetur adipisicing elit, sed do eiusmod tempor incididunt ut labore et dolore magna aliqua. Ut enim ad minim veniam, quis nostrud exercitation ullamco laboris nisi ut aliquip ex ea commodo consequa.Lorem ipsum dolor sit amet, consectetur adipisicing elit, sed do eiusmod tempor incididunt ut labore et dolore magna aliqua. Ut enim ad minim veniam, quis.</p>
    <p>Lorem ipsum dolor sit amet, consectetur adipisicing elit, sed do eiusmod tempor incididunt ut labore et dolore magna aliqua. Ut enim ad minim veniam, quis nostrud exercitation ullamco laboris nisi ut aliquip ex ea commodo consequa.Lorem ipsum dolor sit amet, consectetur adipisicing elit, sed do eiusmod tempor incididunt ut labore et dolore magna aliqua. Ut enim ad minim veniam, quis.</p>
    <p>Lorem ipsum dolor sit amet, consectetur adipisicing elit, sed do eiusmod tempor incididunt ut labore et dolore magna aliqua. Ut enim ad minim veniam, quis nostrud exercitation ullamco laboris nisi ut aliquip ex ea commodo consequa.Lorem ipsum dolor sit amet, consectetur adipisicing elit, sed do eiusmod tempor incididunt ut labore et dolore magna aliqua. Ut enim ad minim veniam, quis.</p>
    <p>Lorem ipsum dolor sit amet, consectetur adipisicing elit, sed do eiusmod tempor incididunt ut labore et dolore magna aliqua. Ut enim ad minim veniam, quis nostrud exercitation ullamco laboris nisi ut aliquip ex ea commodo consequa.Lorem ipsum dolor sit amet, consectetur adipisicing.</p>
  </div>

  <div class="market-copy body-copy">
    <p>Lorem ipsum dolor sit amet, consectetur adipisicing elit, sed do eiusmod tempor incididunt ut labore et dolore magna aliqua. Ut enim ad minim veniam, quis nostrud exercitation ullamco laboris nisi ut aliquip ex ea commodo consequa.Lorem ipsum dolor sit amet, consectetur adipisicing elit, sed do eiusmod tempor incididunt ut labore et dolore magna aliqua. Ut enim ad minim veniam, quis.</p>
    <p>Lorem ipsum dolor sit amet, consectetur adipisicing elit, sed do eiusmod tempor incididunt ut labore et dolore magna aliqua. Ut enim ad minim veniam, quis nostrud exercitation ullamco laboris nisi ut aliquip ex ea commodo consequa.Lorem ipsum dolor sit amet, consectetur adipisicing elit, sed do eiusmod tempor incididunt ut labore et dolore magna aliqua. Ut enim ad minim veniam, quis.</p>
    <p class="spaced">Lorem ipsum dolor sit amet, consectetur adipisicing elit, sed do eiusmod tempor incididunt ut labore et dolore magna aliqua. Ut enim ad minim veniam, quis nostrud exercitation ullamco laboris nisi ut aliquip ex ea commodo.</p>
  </div>

  <svg class="trend-chart" viewBox="650 400 650 500" aria-label="Line chart of rate over period for Area 1 and Area 2">
    <g fill="none" stroke="var(--axis)" stroke-width="3">
      <line x1="748" y1="775" x2="748" y2="448"/>
      <line x1="748" y1="775" x2="1186" y2="775"/>
    </g>
    <polygon points="738,452 758,452 748,438" fill="var(--axis)"/>
    <polygon points="1183,766 1183,784 1199,775" fill="var(--axis)"/>
    <g fill="var(--axis)">
      <circle cx="748" cy="472" r="5"/><circle cx="748" cy="503" r="5"/><circle cx="748" cy="534" r="5"/>
      <circle cx="748" cy="565" r="5"/><circle cx="748" cy="596" r="5"/><circle cx="748" cy="625" r="5"/>
      <circle cx="748" cy="655" r="6"/><circle cx="748" cy="684" r="5"/><circle cx="748" cy="712" r="5"/>
      <circle cx="748" cy="741" r="5"/>
      <circle cx="778" cy="775" r="5"/><circle cx="812" cy="775" r="5"/><circle cx="846" cy="775" r="5"/>
      <circle cx="882" cy="775" r="5"/><circle cx="916" cy="775" r="5"/><circle cx="950" cy="775" r="5"/>
      <circle cx="987" cy="775" r="5"/><circle cx="1021" cy="775" r="5"/><circle cx="1057" cy="775" r="5"/>
      <circle cx="1092" cy="775" r="5"/><circle cx="1126" cy="775" r="5"/><circle cx="1162" cy="775" r="5"/>
    </g>
    <g class="series-area1" stroke="var(--ink)" fill="var(--ink)">
      <polyline fill="none" stroke-width="3" points="782,565 808,680 848,595 883,565 914,627 950,601 989,543 1013,689 1049,664 1089,579 1124,608 1164,524"/>
      <circle cx="782" cy="565" r="4"/><circle cx="808" cy="680" r="4"/><circle cx="848" cy="595" r="4"/>
      <circle cx="883" cy="565" r="4"/><circle cx="914" cy="627" r="4"/><circle cx="950" cy="601" r="4"/>
      <circle cx="989" cy="543" r="4"/><circle cx="1013" cy="689" r="4"/><circle cx="1049" cy="664" r="4"/>
      <circle cx="1089" cy="579" r="4"/><circle cx="1124" cy="608" r="4"/><circle cx="1164" cy="524" r="4"/>
    </g>
    <g class="series-area2" stroke="var(--orange)" fill="var(--orange)">
      <polyline fill="none" stroke-width="3" points="776,682 812,596 848,624 880,537 918,508 951,654 987,595 1022,566 1057,626 1094,597 1126,505 1163,624"/>
      <circle cx="776" cy="682" r="4"/><circle cx="812" cy="596" r="4"/><circle cx="848" cy="624" r="4"/>
      <circle cx="880" cy="537" r="4"/><circle cx="918" cy="508" r="4"/><circle cx="951" cy="654" r="4"/>
      <circle cx="987" cy="595" r="4"/><circle cx="1022" cy="566" r="4"/><circle cx="1057" cy="626" r="4"/>
      <circle cx="1094" cy="597" r="4"/><circle cx="1126" cy="505" r="4"/><circle cx="1163" cy="624" r="4"/>
    </g>
    <text x="680" y="472" font-size="23" fill="var(--ink)">Rate</text>
    <text x="1108" y="810" font-size="23" fill="var(--ink)">Period</text>
    <rect x="706" y="837" width="64" height="6" fill="var(--ink)"/>
    <rect x="706" y="874" width="64" height="6" fill="var(--orange)"/>
    <text x="779" y="850" font-size="29" fill="var(--ink)">Area 1</text>
    <text x="779" y="887" font-size="29" fill="var(--orange)">Area 2</text>
  </svg>

  <footer class="footer">
    <div class="footer-bar"></div>
    <div class="footer-url left">www.harrowfieldestates.example</div>
    <div class="footer-url right">www.harrowfieldestates.example</div>
    <div class="footer-call left"><span class="label">Call : </span><span class="number">000 000 0000</span></div>
    <div class="footer-call right"><span class="label">Call : </span><span class="number">000 000 0000</span></div>
  </footer>

  <div class="page-fold"></div>
</div>
</body>
</html>
```